Anzeigengestaltung für Heilpraktikerin für Psychotherapie
Hallo lurbos, ich bin sehr zufrieden mit dem Design. Danke LG Doris Klemmer
Zielgruppe
Heilpraktikerin für Psychotherapie, Atem- und Körpertherapeutin, Einzelthearpie, Gruppentherapie, Menschen in Lebenskrisen; Menschen, die ihr Leben verändern wollen, Menschen suchen mehr Selbsterfahrung, vorwiegend Frauen, Atersgruppe 20 aufwärts, Menschen mit psychischen Problemen
Entspannung, Berühren, Massieren, Halten, Gespräch, Bewegen, Begleitung Während der Schwangerschaft, Geburt und danach, Trauerbegleitung
Aufgabenstellung
Name und Berufsbezeichnung sind mir wichtig
Praxiseröffnung, Termine nach Vereinbarung
aktuelles Angebot: Fantasiereise- Entspannung von Alltagsstress
sonstiges Angebot: Einzeltherapie/Gruppentherapie,

```html
<!DOCTYPE html>
<html lang="de">
<head>
<meta charset="utf-8">
<title>Praxiseröffnung – Fantasiereise ins Ich</title>
<link href="https://fonts.googleapis.com/css2?family=Cinzel:wght@600;700&family=Open+Sans:wght@300;400&display=swap" rel="stylesheet">
<style>
  :root {
    --magenta: #c8177a;
    --ink: #111111;
    --white: #f4f4f4;
    --brand: #8e3a6c;
    --sky-top: #6f8fb8;
    --sky-mid: #c9d2df;
    --sky-glow: #e9c9a4;
    --sun: #f2b260;
    --dusk: #4a4a58;
    --night: #050505;
  }
  * { margin: 0; padding: 0; box-sizing: border-box; }
  html, body { width: 1200px; height: 822px; overflow: hidden; background: var(--night); }
  .ad {
    position: relative;
    width: 1200px;
    height: 822px;
    overflow: hidden;
    font-family: "Open Sans", sans-serif;
  }
  .ad__scene {
    position: absolute;
    inset: 0;
    background:
      radial-gradient(ellipse 260px 90px at 555px 565px, rgba(255,214,140,0.95), rgba(242,178,96,0.35) 60%, transparent 100%),
      linear-gradient(to bottom,
        var(--sky-top) 0%,
        #93abc9 18%,
        var(--sky-mid) 38%,
        #dcd6d0 52%,
        var(--sky-glow) 62%,
        #b48f78 68%,
        var(--dusk) 74%,
        #1a1a1e 79%,
        var(--night) 84%,
        var(--night) 100%);
  }
  .headline {
    position: absolute;
    left: 0;
    width: 1200px;
    text-align: center;
    font-family: "Cinzel", serif;
  }
  .headline--opening {
    top: 2px;
    font-size: 76px;
    font-weight: 700;
    color: var(--magenta);
    letter-spacing: 1px;
    text-shadow: 1px 2px 2px rgba(0,0,0,0.55);
  }
  .headline--journey {
    top: 86px;
    font-size: 60px;
    line-height: 66px;
    font-weight: 700;
    color: var(--ink);
    letter-spacing: 5px;
  }
  .intro {
    position: absolute;
    top: 210px;
    left: 0;
    width: 1200px;
    text-align: center;
    font-size: 34px;
    line-height: 44px;
    font-weight: 300;
    color: var(--ink);
  }
  .contact {
    position: absolute;
    font-size: 20px;
    line-height: 25.5px;
    font-weight: 300;
    color: var(--white);
  }
  .contact--practice { left: 13px; top: 712px; }
  .contact--reach { right: 13px; top: 737px; text-align: right; }
  .brand {
    position: absolute;
    left: 0;
    width: 1200px;
    top: 764px;
    text-align: center;
    font-size: 36px;
    font-weight: 400;
    color: var(--brand);
    letter-spacing: 1px;
  }
</style>
</head>
<body>
<main class="ad">
  <div class="ad__scene" role="img" aria-label="Foto: Sonnenuntergang hinter Wolken über einer dunklen Waldsilhouette"></div>

  <h1 class="headline headline--opening">PRAXISERÖFFNUNG</h1>
  <h2 class="headline headline--journey">FANTASIEREISE<br>INS ICH...</h2>

  <p class="intro">
    Tauchen Sie ein in die wohltuende<br>
    und entspannende Welt der inneren Bilder.<br>
    Genießen Sie die Ruhe und schöpfen Sie Kraft<br>
    aus den Bildern, die in Ihrem Inneren aufsteigen.<br>
    Einfühlsam führe ich Sie auf&nbsp; Ihre Insel<br>
    der Ruhe und Erholung...
  </p>

  <address class="contact contact--practice" style="font-style:normal">
    Heilpraktikerin für Psychotherapie<br>
    Doris Klemmer<br>
    Lindenweg 14<br>
    73099 Mühlbach
  </address>

  <div class="brand">LichtZeit</div>

  <address class="contact contact--reach" style="font-style:normal">
    lichtzeit.dorisklemmer@postfach.de<br>
    01715550123<br>
    www.lichtzeit-praxis.org
  </address>
</main>
</body>
</html>
```